Etiketten-Design für einen importierten Honig
Zielgruppe
Wir importieren originalen Manuka Honig aus Neuseeland. Der Manuka Honig ist bekannt für seine besonderen Eigenschaften (antibakteriell, etc.). Ein Glas unseres Honigs (500g) kostet zwischen 30 und 150 EUR.
Unsere Zielgruppe sind gesundheitsbewusste Kunden, die wenig preissensibel sind. Überwiegend wird der Manuka Honig im Fachhandel (z.B. Reformhaus, Drogerie, Biomarkt, etc.) verkauft. Der Großteil unserer Kunden ist 30+ Jahre.
Aufgabenstellung
Bei dem Etikett handelt es sich um das erste Produktetikett. Damit ist in der Farbgestaltung noch alles offen. Das Logo und der Name ist jedoch fix.
Das Etikett ist wird auf einem bpa-freien schwarzen Plastikbehälter angebracht. Dieser ist bei Manuka Honigen Standard aufgrund des langen Transports von Neuseeland nach Deutschland (gerne googeln). Der Deckel dieses Behälters ist schwarz.
Nachdem es sich um ein hochpreisiges Produkt handelt, soll das Etikett diese hohe Wertigkeit widerspiegeln. Damit ist eine Veredelung des Etiketts notwendig. Viele Konkurrenten arbeiten mit Gold, alternative Farben sind jedoch auch möglich.
Das Etikett überdeckt drei der vier Seiten des Plastikbehälters (vorne + links + rechts). Die Maße sind 160 mm x 60 mm. Zusätzlich zu den Etikettenmaßen bitte 2 mm Beschnittzugabe je Seite hinzufügen.
Hintergrundinformationen zu unserer Marke:
- Der Markenname lautet Tavolin. Der Markenname leitet sich von der ersten Imkerin Neuseelands ab - Greta Lonfeld. Sie hatte im Jahr 1839 die ersten Bienenstöcke nach Neuseeland gebracht und den ersten Manuka Honig geerntet.
- Unser Logo ist eine Verbindung einer Frau und den neuseeländischen Farn. Dieses Logo stellt also direkt eine Verbindung zu Neuseeland dar.
- Unsere Marke Tavolin ist eine qualitativ hochwertige, luxuriöse und hochpreisige Marke. Genau wie in dem Logo selbst, sollen diese Verbindungen zu Neuseeland, der Natur (Honig ist ein Naturprodukt) und Greta Lonfeld auch auf dem Etikett zu finden sein.
Wonach suchen wir:
- Wir sind auf der Suche nach einem einzigartigen Design, der unseren Honig besonders hervorhebt. Das Etikett soll auffällig sein und uns von anderen unterscheiden. (Eye-catching)
- Eine Veredelung des Etiketts ist Pflicht, da dies für uns die Wertigkeit des Etiketts und des Produktes stark erhöht. In welcher Art die Veredelung durchgeführt wird, ist Ihnen überlassen.
Das dürfen Sie frei wählen:
- Bisher haben..

```html
<!DOCTYPE html>
<html lang="de">
<head>
<meta charset="utf-8">
<title>Tavolin Manuka Honig – Etikett</title>
<link rel="stylesheet" href="https://fonts.googleapis.com/css2?family=Lato:wght@300;400;700;900&display=swap">
<style>
  :root {
    --page: #ffffff;
    --panel: #2b2b2b;
    --border-band: #7b7b7b;
    --border-line: #d9d9d9;
    --text: #ffffff;
    --gold: #f7a800;
    --honey-light: #ffc81a;
    --honey-dark: #f59a00;
    --ink: #1b1b1b;
  }
  * { margin: 0; padding: 0; box-sizing: border-box; }
  html, body {
    width: 1200px; height: 751px; overflow: hidden;
    background: var(--page);
    font-family: "Lato", sans-serif;
    color: var(--text);
  }
  .canvas { position: relative; width: 1200px; height: 751px; }

  .label {
    position: absolute; left: 117px; top: 238px; width: 967px; height: 367px;
  }
  .label__border {
    position: absolute; inset: 0;
    background: var(--border-band);
  }
  .label__panel {
    position: absolute; left: 16px; top: 16px; right: 15px; bottom: 16px;
    background: var(--panel);
    outline: 1px solid var(--border-line);
  }

  /* Left column: nutrition */
  .nutrition {
    position: absolute; left: 176px; top: 274px; width: 191px;
  }
  .nutrition__title {
    position: absolute; left: 0; right: -10px; text-align: center;
    font-size: 11px; font-weight: 700; letter-spacing: 0.3px; top: 0;
  }
  .nutrition__table {
    position: absolute; top: 19px; left: 0; width: 191px;
    font-size: 11px; font-weight: 400; line-height: 14.3px;
  }
  .nutrition__row { display: flex; justify-content: space-between; }
  .nutrition__row--sub .nutrition__name { padding-left: 7px; }

  .storage-note, .infant-warning {
    position: absolute; left: 158px; width: 226px; text-align: center;
    font-size: 8.5px; line-height: 10.3px; letter-spacing: 0.2px;
  }
  .storage-note { top: 403px; }
  .infant-warning { top: 434px; text-transform: uppercase; }
  .net-weight {
    position: absolute; left: 158px; width: 226px; top: 466px; text-align: center;
    font-size: 18px; font-weight: 700; color: var(--gold);
  }
  .net-weight__e { font-weight: 300; font-size: 21px; margin-right: 3px; }
  .sticker-field {
    position: absolute; left: 158px; top: 501px; width: 226px; height: 104px;
    background: #ffffff;
  }

  /* Centre medallion */
  .medallion { position: absolute; left: 433px; top: 253px; width: 336px; height: 336px; }
  .medallion svg { display: block; }
  .brand-mark {
    position: absolute; left: 583px; top: 350px; width: 36px; height: 36px;
    border-radius: 50%; background: #ffffff;
  }
  .brand-name {
    position: absolute; left: 511px; width: 180px; top: 399px; text-align: center;
    font-size: 17px; font-weight: 400; letter-spacing: 1px; color: #ffffff;
  }
  .product-name {
    position: absolute; left: 505px; width: 192px; top: 426px; text-align: center;
    font-size: 33px; font-weight: 900; line-height: 31px; letter-spacing: 0.5px;
  }
  .product-name__top { color: var(--ink); }
  .product-name__bottom { color: #ffffff; }

  /* Right column: story */
  .story { position: absolute; left: 781px; width: 280px; top: 272px; text-align: center; }
  .story__title {
    font-size: 17.5px; font-weight: 900; color: var(--gold);
    line-height: 21px; letter-spacing: 0.3px;
  }
  .story__text {
    margin-top: 13px; font-size: 12.5px; font-weight: 700; line-height: 15.6px; letter-spacing: 0.3px;
  }
  .story__text + .story__text { margin-top: 15px; }
  .story__meta {
    margin-top: 16px; font-size: 10.5px; line-height: 13px; letter-spacing: 0.3px;
  }
  .story__meta + .story__meta { margin-top: 11px; }
</style>
</head>
<body>
<main class="canvas">
  <section class="label">
    <div class="label__border" role="img" aria-label="Feines grau-weißes Zickzack-Muster als Etikettenrand"></div>
    <div class="label__panel"></div>
  </section>

  <section class="nutrition">
    <h2 class="nutrition__title">Nährwertangaben pro 100 g</h2>
    <div class="nutrition__table">
      <div class="nutrition__row"><span class="nutrition__name">Energie</span><span>1400 kJ / 329 kcal</span></div>
      <div class="nutrition__row"><span class="nutrition__name">Fett</span><span>0,8g</span></div>
      <div class="nutrition__row nutrition__row--sub"><span class="nutrition__name">davon gesättigte Fettsäuren</span><span>0,5g</span></div>
      <div class="nutrition__row"><span class="nutrition__name">Kohlenhydrate</span><span>80,4g</span></div>
      <div class="nutrition__row nutrition__row--sub"><span class="nutrition__name">davon Zucker</span><span>65,4g</span></div>
      <div class="nutrition__row"><span class="nutrition__name">Eiweiß</span><span>0,1g</span></div>
      <div class="nutrition__row"><span class="nutrition__name">Salz</span><span>0,02g</span></div>
    </div>
  </section>
  <p class="storage-note">1 Portion = 10g, Trocken, dunkel und<br>nicht über 25 °C lagern.</p>
  <p class="infant-warning">Honig ist für Säuglinge unter<br>12 Monaten nicht geeignet</p>
  <p class="net-weight"><span class="net-weight__e">e</span>500g</p>
  <div class="sticker-field"></div>

  <div class="medallion">
    <svg width="336" height="336" viewBox="0 0 336 336">
      <defs>
        <radialGradient id="ornamentTone" cx="50%" cy="50%" r="50%">
          <stop offset="75%" stop-color="#4a4a4a"/>
          <stop offset="90%" stop-color="#7a7a7a"/>
          <stop offset="100%" stop-color="#3a3a3a"/>
        </radialGradient>
        <linearGradient id="honeyTone" x1="0" y1="0" x2="0" y2="1">
          <stop offset="0%" stop-color="var(--honey-light)"/>
          <stop offset="100%" stop-color="var(--honey-dark)"/>
        </linearGradient>
      </defs>
      <circle cx="168" cy="168" r="167" fill="#ffffff"/>
      <g role="img" aria-label="Schwarz-weißer Ring aus Maori-Ornamenten">
        <circle cx="168" cy="168" r="154" fill="url(#ornamentTone)"/>
        <circle cx="168" cy="168" r="129" fill="#ffffff"/>
      </g>
      <circle cx="168" cy="168" r="124" fill="none" stroke="#111" stroke-width="3"/>
      <circle cx="168" cy="168" r="119" fill="none" stroke="#555" stroke-width="2"/>
      <circle cx="168" cy="168" r="115" fill="none" stroke="#111" stroke-width="1.5"/>
      <polygon points="168,55 258,104 258,223 168,248 78,223 78,104" fill="url(#honeyTone)" stroke="#ffd24a" stroke-width="2" stroke-linejoin="round"/>
    </svg>
  </div>
  <div class="brand-mark"></div>
  <p class="brand-name">TAVOLIN</p>
  <h1 class="product-name"><span class="product-name__top">MANUKA</span><br><span class="product-name__bottom">HONIG</span></h1>

  <section class="story">
    <h2 class="story__title">MANUKA HONIG –<br>DAS GOLD DER MAORI</h2>
    <p class="story__text">Bereits die Ureinwohner Neuseelands, die Maori, wussten um die Kostbarkeit des Manuka Honigs und nutzten ihn für seine besonderen Eigenschaften.</p>
    <p class="story__text">Der Anteil des in diesem Honig enthaltenen Wirkstoffs Methylglyoxal (MGO) wurde durch ein akkreditiertes Labor auf mindestens<br>450 mg/kg geprüft.</p>
    <p class="story__meta">Inhalt:<br>100 % Manuka Honig aus Neuseeland</p>
    <p class="story__meta">Importiert und vertrieben durch:<br>Kaurimo GmbH, Lindenweg 12,<br>95690 Waldbrunnen</p>
  </section>
</main>
</body>
</html>
```